Eye Catching Wrap for Keystone Plumbing

We would like a truck wrap (box truck/transit) that is distinguishable, unique, and eye catching. Stick with the basic colors within the logo but feel free to add more as long as it’s not over done. Must include the following:
-phone number (big and bold 555-872-3096)
-logo
-“Keystone Quality Guaranteed” (or your own slogan if it’s better
-military and first responder discounts
-website

```html
<!DOCTYPE html>
<html lang="en">
<head>
<meta charset="utf-8">
<title>Keystone Plumbing – Van Wrap</title>
<link rel="stylesheet" href="https://fonts.googleapis.com/css2?family=Anton&family=Oswald:wght@500;700&family=Yellowtail&display=swap">
<style>
  :root {
    --backdrop: #d9dbdf;
    --wrap-black: #0c0c0e;
    --wrap-charcoal: #1a1a1e;
    --orange: #e8742a;
    --orange-deep: #b9501a;
    --orange-dark: #4e220c;
    --blue-bright: #35c2ee;
    --blue-royal: #1c4fd8;
    --red-accent: #d8331f;
    --white: #ffffff;
  }
  * { margin: 0; padding: 0; box-sizing: border-box; }
  html, body { width: 1200px; height: 2700px; overflow: hidden; }
  body { background: var(--backdrop); position: relative; font-family: "Oswald", sans-serif; }

  .wrap-panel {
    position: absolute;
    border-radius: 40px;
    overflow: hidden;
    background: var(--wrap-black);
    box-shadow: 0 10px 30px rgba(0,0,0,.25);
  }
  .side-driver {
    left: 50px; top: 60px; width: 1100px; height: 560px;
    background: linear-gradient(90deg, var(--wrap-black) 0%, var(--wrap-charcoal) 52%, var(--orange-dark) 62%, var(--orange-deep) 72%, var(--orange) 84%, var(--orange-deep) 95%, var(--orange-dark) 100%);
  }
  .side-passenger {
    left: 50px; top: 700px; width: 1100px; height: 560px;
    background: linear-gradient(270deg, var(--wrap-black) 0%, var(--wrap-charcoal) 52%, var(--orange-dark) 62%, var(--orange-deep) 72%, var(--orange) 84%, var(--orange-deep) 95%, var(--orange-dark) 100%);
  }
  .rear-doors {
    left: 170px; top: 1340px; width: 860px; height: 1300px;
    background: linear-gradient(180deg, var(--wrap-charcoal) 0%, var(--wrap-black) 40%, var(--orange-dark) 75%, var(--orange-deep) 100%);
  }
  .door-seam { position: absolute; left: 50%; top: 0; bottom: 0; width: 3px; background: rgba(0,0,0,.6); }

  .rocker-stripe { position: absolute; left: 0; right: 0; bottom: 40px; height: 6px; background: var(--orange); opacity: .85; }

  .wordmark {
    position: absolute;
    font-family: "Anton", sans-serif;
    color: var(--blue-bright);
    line-height: .95;
    text-align: center;
    letter-spacing: 2px;
    white-space: nowrap;
  }
  .wordmark-line { display: block; }
  .wordmark-sub {
    position: absolute;
    font-family: "Oswald", sans-serif;
    font-weight: 700;
    color: var(--blue-royal);
    text-align: center;
    letter-spacing: 3px;
    white-space: nowrap;
  }

  .discount-block { position: absolute; text-align: center; color: var(--white); white-space: nowrap; }
  .discount-stars { font-size: 40px; letter-spacing: 6px; line-height: 1; }
  .discount-stars .star-lead { font-size: 54px; }
  .discount-text {
    font-family: "Anton", sans-serif;
    font-size: 32px; line-height: 1.1;
    transform: skewX(-10deg);
    text-shadow: 2px 2px 0 var(--blue-royal);
  }
  .flag-rule { margin: 10px auto 0; width: 150px; height: 8px;
    background: linear-gradient(180deg, var(--red-accent) 0 33%, var(--white) 33% 66%, var(--blue-royal) 66%); }

  .contact-block { position: absolute; color: var(--white); white-space: nowrap; }
  .contact-web {
    font-family: "Oswald", sans-serif; font-weight: 700; font-size: 32px;
    transform: skewX(-10deg); text-shadow: 2px 2px 0 var(--blue-royal);
  }
  .contact-phone {
    font-family: "Anton", sans-serif; font-size: 70px; line-height: 1.05;
    transform: skewX(-10deg); text-shadow: 3px 3px 0 var(--blue-royal);
  }

  .slogan { position: absolute; white-space: nowrap; }
  .slogan-name {
    font-family: "Anton", sans-serif; font-size: 30px; color: var(--blue-royal);
    transform: skewX(-10deg); display: block; margin-left: 60px;
  }
  .slogan-script {
    font-family: "Yellowtail", cursive; font-size: 58px; color: var(--red-accent); line-height: 1;
  }
  .slogan-script .bang { color: var(--blue-bright); }
</style>
</head>
<body>

  <section class="wrap-panel side-driver" aria-label="Driver side panel">
    <div class="wordmark" style="left:320px; top:120px; width:520px; font-size:96px;">
      <span class="wordmark-line">KEYSTONE</span>
      <span class="wordmark-line">PLUMBING</span>
    </div>
    <div class="wordmark-sub" style="left:320px; top:318px; width:520px; font-size:20px;">HEATING AND COOLING</div>

    <div class="discount-block" style="left:820px; top:50px; width:260px;">
      <div class="discount-stars">★★<span class="star-lead">★</span>★★</div>
      <div class="discount-text">MILITARY AND<br>FIRST RESPONDER<br>DISCOUNTS</div>
      <div class="flag-rule"></div>
    </div>

    <div class="contact-block" style="left:620px; top:360px; width:450px; text-align:right;">
      <div class="contact-web">KeystonePlumbing.com</div>
      <div class="contact-phone">555-872-3096</div>
    </div>

    <div class="slogan" style="left:60px; top:380px;">
      <span class="slogan-name">Keystone</span>
      <span class="slogan-script">Quality Guaranteed<span class="bang">!</span></span>
    </div>
    <div class="rocker-stripe"></div>
  </section>

  <section class="wrap-panel side-passenger" aria-label="Passenger side panel">
    <div class="wordmark" style="left:260px; top:120px; width:520px; font-size:96px;">
      <span class="wordmark-line">KEYSTONE</span>
      <span class="wordmark-line">PLUMBING</span>
    </div>
    <div class="wordmark-sub" style="left:260px; top:318px; width:520px; font-size:20px;">HEATING AND COOLING</div>

    <div class="discount-block" style="left:20px; top:50px; width:260px;">
      <div class="discount-stars">★★<span class="star-lead">★</span>★★</div>
      <div class="discount-text">MILITARY AND<br>FIRST RESPONDER<br>DISCOUNTS</div>
      <div class="flag-rule"></div>
    </div>

    <div class="contact-block" style="left:30px; top:360px; width:450px;">
      <div class="contact-web">KeystonePlumbing.com</div>
      <div class="contact-phone">555-872-3096</div>
    </div>

    <div class="slogan" style="left:580px; top:380px;">
      <span class="slogan-name">Keystone</span>
      <span class="slogan-script">Quality Guaranteed<span class="bang">!</span></span>
    </div>
    <div class="rocker-stripe"></div>
  </section>

  <section class="wrap-panel rear-doors" aria-label="Rear doors panel">
    <div class="door-seam"></div>

    <div class="slogan" style="left:450px; top:50px; transform:scale(.7); transform-origin:left top;">
      <span class="slogan-name">Keystone</span>
      <span class="slogan-script">Quality Guaranteed<span class="bang">!</span></span>
    </div>

    <div class="wordmark" style="left:130px; top:380px; width:600px; font-size:110px;">
      <span class="wordmark-line">KEYSTONE</span>
      <span class="wordmark-line">PLUMBING</span>
    </div>

    <div class="discount-block" style="left:70px; top:900px; width:290px;">
      <div class="discount-stars">★★<span class="star-lead">★</span>★★</div>
      <div class="discount-text">MILITARY AND<br>FIRST RESPONDER<br>DISCOUNTS</div>
      <div class="flag-rule"></div>
    </div>

    <div class="contact-block" style="left:455px; top:930px; width:370px; text-align:center;">
      <div class="contact-web" style="font-size:28px;">KeystonePlumbing.com</div>
      <div class="contact-phone" style="font-size:56px;">555-872-3096</div>
    </div>
  </section>

</body>
</html>
```